UI Improvement for FlorvaLink app

We are looking for a talented UI/UX designer to REFINE and enhance the visual design of our mobile application, FlorvaLink. The app is fully functional, but we need a designer to improve its aesthetics by specifying design elements such as fonts, colors, spacing, and component styles.
Your task will be to analyze the CURRENT UI and provide detailed design specifications that will make the app more visually appealing, modern, and user-friendly.
TODO:
Review the existing FlorvaLink app design (see attachments) and identify areas for visual improvement.
Provide a detailed UI style guide, including:
Typography (font choices, sizes, and weights)
Color palette (primary, secondary, and accent colors)
Component styling (buttons, forms, icons, and interactive elements)
Spacing and layout guidelines (margins, paddings, and alignment)
Ensure the design remains clean, modern, and professional while maintaining usability and accessibility.
Provide design mockups or visual examples (if possible) to illustrate the proposed changes.
Deliverables:
A UI Style Guide (PDF or Figma file) with specifications on fonts, colors, spacing, and UI components.
Optionally, before/after mockups or examples demonstrating the improvements.
Ideal Designer:
Strong experience in mobile UI/UX design.
Understanding of modern design trends and best practices.
Ability to communicate design choices clearly for easy developer implementation.
I have attached 7 images showcasing the main UI screens used in the FlorvaLink app. These screens need visual enhancements to improve their overall look and user experience.
The images represent the current design in three key modes:
LIST Mode – Displays data in a structured list format.
READ Mode – Shows detailed information when a user selects an item.
ADD/EDIT Mode – Allows users to input or modify information.
Additionally, there is a ‘MORE’ page, which serves as a menu listing other features of the application.
Task Objective:
Please refine and improve these UIs to create a more modern, visually appealing, and user-friendly experience. Focus on typography, colors, spacing, and component styling to ensure a cohesive and polished design.
Look and feel
Each slider illustrates characteristics of the customer's brand and the style your logo design should communicate.

```html
<!DOCTYPE html>
<html lang="en">
<head>
<meta charset="utf-8">
<title>FlorvaLink app – Read Page</title>
<link href="https://fonts.googleapis.com/css2?family=Figtree:wght@400;500;600;700&family=Nunito+Sans:wght@400;600;700;800&display=swap" rel="stylesheet">
<style>
  :root{
    --blue:#1B7ECC; --ink:#1C1F34; --slate:#4B4B5A; --gray:#636669; --mute:#7C848B;
    --bg:#F2F2F7; --line:#E2E7F1;
    --cyan:#25C2E3; --green:#29BA85; --orange:#F77E53; --yellow:#FFBE0B; --pink:#FF5C75; --purple:#7859F4;
    --legacy-bg:#E9E9EE; --legacy-link:#2E63C9; --chip:#EEF2FA;
  }
  html,body{margin:0;padding:0}
  body{width:1200px;height:1118px;overflow:hidden;background:#fff}
  .board{position:relative;width:1988px;height:1852px;transform:scale(.6036);transform-origin:0 0;font-family:'Nunito Sans',sans-serif;color:var(--ink)}
  .abs{position:absolute}
  .m{transform:translateY(-50%)}

  .sheet-title{position:absolute;left:82px;top:78px;margin:0;font:700 58px/1 'Figtree',sans-serif;color:#000;letter-spacing:-.5px}
  .group-label{position:absolute;top:227px;font:600 20px/1 'Figtree',sans-serif;color:var(--gray)}
  .swatch{position:absolute;width:54px;height:54px;border-radius:3px;color:#fff;font:400 12px/1 'Nunito Sans',sans-serif;display:flex;align-items:center;justify-content:center}
  .swatch.light{color:var(--slate)}
  .font-sample{position:absolute;left:541px;font-size:46px;line-height:1;color:#000}
  .band{position:absolute;left:81px;top:542px;width:1826px;height:50px;background:var(--blue);color:#fff;font:700 20px/50px 'Figtree',sans-serif;padding-left:14px;box-sizing:border-box}

  /* legacy screens */
  .legacy{position:absolute;width:264px;background:var(--legacy-bg);overflow:hidden;font-family:'Nunito Sans',sans-serif}
  .legacy .status{position:absolute;left:0;top:0;width:100%;height:33px;background:#000;color:#fff;z-index:3}
  .legacy .status .time{position:absolute;left:39px;top:9px;font:600 12px/1 'Nunito Sans',sans-serif}
  .legacy .status svg{position:absolute;right:24px;top:12px}
  .legacy .appbar{position:absolute;left:0;top:33px;width:100%;height:38px;background:#F4F4F7;z-index:3;font-size:12px;color:#222;text-align:center;line-height:38px;border-bottom:1px solid #ddd;box-sizing:border-box}
  .legacy .appbar .back{position:absolute;left:12px;top:13px}
  .legacy .appbar .dots{position:absolute;right:12px;top:0;font-weight:800;letter-spacing:1px;font-size:11px}
  .card{position:absolute;left:4px;right:4px;background:#fff;border-radius:2px}
  .lg-add{position:absolute;left:10px;font-size:10.5px;color:#222;display:flex;align-items:center;gap:3px;transform:translateY(-50%);white-space:nowrap}
  .ring{width:8px;height:8px;border:1px solid var(--legacy-link);border-radius:50%;position:relative;display:inline-block}
  .ring::before,.ring::after{content:"";position:absolute;background:var(--legacy-link);left:50%;top:50%;transform:translate(-50%,-50%)}
  .ring::before{width:5px;height:1px}.ring::after{width:1px;height:5px}
  .lg-title{position:absolute;left:10px;font-weight:800;font-size:10px;color:#111;transform:translateY(-50%)}
  .lg-collapse{position:absolute;right:10px;font-size:9px;color:#b0b0b0;transform:translateY(-50%)}
  .lg-text{position:absolute;left:10px;right:26px;font-size:10.5px;line-height:12px;color:#222;transform:translateY(-50%)}
  .lg-rule{position:absolute;left:10px;right:10px;height:1px;background:#d9d9d9}
  .lg-chev{position:absolute;right:12px}
  .lg-label{position:absolute;font-size:7.5px;color:var(--legacy-link);line-height:1;transform:translateY(-50%);white-space:nowrap}
  .lg-val{position:absolute;font-size:10.5px;color:#111;line-height:11px;transform:translateY(-50%);white-space:nowrap}
  .lg-dots{position:absolute;right:12px;font-weight:800;font-size:10px;letter-spacing:1px;transform:translateY(-50%)}
  .tool{position:absolute;top:81px;width:30px;height:28px;border:1px solid #cfcfd4;border-radius:4px;background:#fff;font-size:6px;color:#333;text-align:center;box-sizing:border-box;padding-top:4px;line-height:1}
  .tool i{display:block;width:7px;height:5px;margin:0 auto 5px;border-top:1px solid #333;border-bottom:1px solid #333}
  .tabs{position:absolute;left:0;right:0;background:#fff;display:flex;z-index:3}
  .tab{flex:1;text-align:center;font-size:8px;color:#222;padding-top:3px}
  .tab svg{display:block;margin:0 auto 3px}
  .tab.active{color:var(--blue)}
  .home{position:absolute;height:3px;border-radius:2px;background:#111;z-index:4}

  /* redesigned screens */
  .phone{position:absolute;background:#fff;border-radius:36px;box-shadow:0 0 0 10px #111;overflow:hidden;font-family:'Nunito Sans',sans-serif}
  .phone .clock{position:absolute;left:25px;top:20px;transform:translateY(-50%);font:600 13px/1 'Figtree',sans-serif;color:#000}
  .phone .sys{position:absolute;right:20px;top:14px}
  .top-icon{position:absolute;transform:translateY(-50%)}
  .more{position:absolute;right:14px;color:var(--blue);font-weight:800;font-size:13px;letter-spacing:1.5px;transform:translateY(-50%);line-height:1}
  .avatar{position:absolute;width:38px;height:38px;border-radius:50%;color:#fff;font:700 13px/38px 'Figtree',sans-serif;text-align:center}
  .kicker{position:absolute;font-size:11px;color:var(--mute);transform:translateY(-50%)}
  .headline{position:absolute;font:700 20px/1 'Figtree',sans-serif;color:var(--ink);transform:translateY(-50%);white-space:nowrap}
  .sec{position:absolute;left:11px;right:12px;display:flex;align-items:center;justify-content:space-between;transform:translateY(-50%);font-weight:700;font-size:12px;color:var(--ink)}
  .act{display:flex;align-items:center;gap:7px;color:var(--blue);font-weight:400;font-size:12px}
  .plus{width:11px;height:11px;border:1.3px solid var(--blue);border-radius:50%;position:relative}
  .plus::before,.plus::after{content:"";position:absolute;background:var(--blue);left:50%;top:50%;transform:translate(-50%,-50%)}
  .plus::before{width:6px;height:1.3px}.plus::after{width:1.3px;height:6px}
  .sep{width:1px;height:14px;background:#e6e8ee}
  .rule{position:absolute;left:0;right:0;height:1px;background:#ECEEF3}
  .chip{position:absolute;left:11px;right:11px;background:var(--chip);border-radius:6px;padding:0 11px;font-size:12.5px;line-height:15px;color:var(--slate);display:flex;flex-direction:column;justify-content:center;box-sizing:border-box}
  .dot{color:#a7adb8;padding:0 3px}
  .f-label{position:absolute;left:22px;font-size:9.5px;color:var(--mute);transform:translateY(-50%);white-space:nowrap}
  .f-value{position:absolute;left:22px;right:14px;font-size:13px;line-height:14px;color:var(--ink);transform:translateY(-50%)}
  .f-value.ok{color:var(--green)}
  .indicator{position:absolute;height:4px;border-radius:2px;background:#111}
</style>
</head>
<body>
<div class="board">

  <h1 class="sheet-title">FlorvaLink app</h1>

  <div class="group-label" style="left:81px">Colors</div>
  <div class="swatch" style="left:81px;top:267px;background:var(--blue)">1B7ECC</div>
  <div class="swatch" style="left:146px;top:267px;background:var(--ink)">1C1F34</div>
  <div class="swatch" style="left:211px;top:267px;background:var(--slate)">4B4B5A</div>
  <div class="swatch" style="left:276px;top:267px;background:var(--gray)">636669</div>
  <div class="swatch" style="left:341px;top:267px;background:var(--mute)">7C848B</div>
  <div class="swatch light" style="left:81px;top:337px;background:var(--bg)">F2F2F7</div>
  <div class="swatch light" style="left:146px;top:337px;background:var(--line)">E2E7F1</div>
  <div class="swatch" style="left:81px;top:407px;background:var(--cyan)">25C2E3</div>
  <div class="swatch" style="left:146px;top:407px;background:var(--green)">29BA85</div>
  <div class="swatch" style="left:211px;top:407px;background:var(--orange)">F77E53</div>
  <div class="swatch" style="left:276px;top:407px;background:var(--yellow)">FFBE0B</div>
  <div class="swatch" style="left:341px;top:407px;background:var(--pink)">FF5C75</div>
  <div class="swatch" style="left:406px;top:407px;background:var(--purple)">7859F4</div>

  <div class="group-label" style="left:541px">Fonts</div>
  <div class="font-sample" style="top:270px;font-family:'Figtree',sans-serif">Figtree</div>
  <div class="font-sample" style="top:341px;font-family:'Nunito Sans',sans-serif">Nunito Sans</div>

  <div class="band">Read Page</div>

  <!-- Contact, legacy list (upper) -->
  <section class="legacy" style="left:81px;top:619px;height:569px">
    <div class="status"><span class="time">3:13</span>
      <svg width="30" height="9" viewBox="0 0 30 9"><path d="M4 7a5 5 0 0 1 6 0M2 5a8 8 0 0 1 10 0" stroke="#fff" fill="none" stroke-width="1.3"/><rect x="16" y="1" width="12" height="7" rx="1.5" fill="#fff"/></svg></div>
    <div class="appbar"><svg class="back" width="11" height="11" viewBox="0 0 11 11"><path d="M10 5.5H1M5 1 1 5.5 5 10" stroke="#222" fill="none" stroke-width="1.3"/></svg>Contact<span class="dots">•••</span></div>
    <div class="card" style="top:59px;height:32px"></div>
    <div class="card" style="top:78px;height:32px"></div><div class="lg-add" style="top:94px"><i class="ring"></i>Add Email -e</div>
    <div class="card" style="top:116px;height:32px"></div><div class="lg-add" style="top:132px"><i class="ring"></i>Add Social Media -e</div>
    <div class="card" style="top:154px;height:32px"></div><div class="lg-add" style="top:170px"><i class="ring"></i>Add Emergency Contact -e</div>
    <div class="card" style="top:192px;height:32px"></div><div class="lg-add" style="top:208px"><i class="ring"></i>Add Personal Information -e</div>
    <div class="card" style="top:230px;height:32px"></div><div class="lg-add" style="top:246px"><i class="ring"></i>Add Work Info -e</div>
    <div class="card" style="top:268px;height:32px"></div><div class="lg-add" style="top:284px"><i class="ring"></i>Add Skills/Talents -e</div>
    <div class="card" style="top:306px;height:32px"></div><div class="lg-add" style="top:322px"><i class="ring"></i>Add Resources -e</div>
    <div class="card" style="top:338px;height:73px;background:#FEFBE0"></div>
    <div class="lg-title" style="top:354px">Pilots -e</div><div class="lg-collapse" style="top:354px">Collapse</div>
    <div class="lg-text" style="top:384px">Marlow, Dean, 3647946, 10/31/23</div>
    <svg class="lg-chev" style="top:376px" width="10" height="6" viewBox="0 0 10 6"><path d="M1 1l4 4 4-4" stroke="#bbb" fill="none"/></svg>
    <div class="lg-rule" style="top:406px"></div>
    <div class="card" style="top:419px;height:110px;background:#DCFCFF"></div>
    <div class="lg-title" style="top:435px">Aircraft Owner -e</div><div class="lg-collapse" style="top:435px">Collapse</div>
    <div class="lg-text" style="top:471px">Personal: Marlow, Dean: Aerolyn: 182T: Aerolyn Aircraft Company, Single Engine, 1100</div>
    <svg class="lg-chev" style="top:457px" width="10" height="6" viewBox="0 0 10 6"><path d="M1 1l4 4 4-4" stroke="#bbb" fill="none"/></svg>
    <div class="lg-rule" style="top:496px"></div>
    <div class="lg-add" style="top:518px"><i class="ring"></i>Add Aircraft Owner -e</div>
    <nav class="tabs" style="top:519px;height:50px">
      <div class="tab active"><svg width="10" height="10" viewBox="0 0 10 10"><circle cx="5" cy="3" r="2.3" fill="currentColor"/><path d="M1 10a4 3.5 0 0 1 8 0z" fill="currentColor"/></svg>Contact</div>
      <div class="tab"><svg width="10" height="10" viewBox="0 0 10 10"><circle cx="5" cy="3" r="2.3" fill="currentColor"/><path d="M1 10a4 3.5 0 0 1 8 0z" fill="currentColor"/></svg>Pilot</div>
      <div class="tab"><svg width="10" height="10" viewBox="0 0 10 10"><path d="M5 0l1 4 4 2v1l-4-1-0.5 2.5 1.5 1V10L5 9.3 3 10v-.5l1.5-1L4 6 0 7V6l4-2z" fill="currentColor"/></svg>Plane</div>
      <div class="tab"><svg width="10" height="10" viewBox="0 0 10 10"><rect x="2" y="3" width="6" height="6" rx="1.5" fill="currentColor"/><rect x="4" y="0" width="2" height="4" fill="currentColor"/></svg>Flt Request</div>
      <div class="tab"><svg width="10" height="10" viewBox="0 0 10 10"><circle cx="2" cy="5" r="1" fill="currentColor"/><circle cx="5" cy="5" r="1" fill="currentColor"/><circle cx="8" cy="5" r="1" fill="currentColor"/></svg>More</div>
    </nav>
    <div class="home" style="left:85px;width:94px;top:563px"></div>
  </section>

  <!-- Contact, legacy list (lower) -->
  <section class="legacy" style="left:81px;top:1197px;height:573px">
    <div class="status"><span class="time">3:14</span>
      <svg width="30" height="9" viewBox="0 0 30 9"><path d="M4 7a5 5 0 0 1 6 0M2 5a8 8 0 0 1 10 0" stroke="#fff" fill="none" stroke-width="1.3"/><rect x="16" y="1" width="12" height="7" rx="1.5" fill="#fff"/></svg></div>
    <div class="appbar"><svg class="back" width="11" height="11" viewBox="0 0 11 11"><path d="M10 5.5H1M5 1 1 5.5 5 10" stroke="#222" fill="none" stroke-width="1.3"/></svg>Contact<span class="dots">•••</span></div>
    <div class="card" style="top:66px;height:32px"></div><div class="lg-add" style="top:84px"><i class="ring"></i>Add Personal Information -e</div>
    <div class="card" style="top:106px;height:32px"></div><div class="lg-add" style="top:122px"><i class="ring"></i>Add Work Info -e</div>
    <div class="card" style="top:144px;height:32px"></div><div class="lg-add" style="top:160px"><i class="ring"></i>Add Skills/Talents -e</div>
    <div class="card" style="top:182px;height:32px"></div><div class="lg-add" style="top:198px"><i class="ring"></i>Add Resources -e</div>
    <div class="card" style="top:216px;height:75px;background:#FEFBE0"></div>
    <div class="lg-title" style="top:230px">Pilots -e</div><div class="lg-collapse" style="top:230px">Collapse</div>
    <div class="lg-text" style="top:259px">Marlow, Dean, 3647946, 10/31/23</div>
    <svg class="lg-chev" style="top:252px" width="10" height="6" viewBox="0 0 10 6"><path d="M1 1l4 4 4-4" stroke="#bbb" fill="none"/></svg>
    <div class="lg-rule" style="top:283px"></div>
    <div class="card" style="top:295px;height:112px;background:#DCFCFF"></div>
    <div class="lg-title" style="top:311px">Aircraft Owner -e</div><div class="lg-collapse" style="top:311px">Collapse</div>
    <div class="lg-text" style="top:346px">Personal: Marlow, Dean: Aerolyn: 182T: Aerolyn Aircraft Company, Single Engine, 1100</div>
    <svg class="lg-chev" style="top:333px" width="10" height="6" viewBox="0 0 10 6"><path d="M1 1l4 4 4-4" stroke="#bbb" fill="none"/></svg>
    <div class="lg-rule" style="top:373px"></div>
    <div class="lg-add" style="top:393px"><i class="ring"></i>Add Aircraft Owner -e</div>
    <div class="card" style="top:411px;height:108px;background:#8FEA8F"></div>
    <div class="lg-title" style="top:425px">Qualified Pilot -e</div><div class="lg-collapse" style="top:425px">Collapse</div>
    <div class="lg-text" style="top:460px">Marlow, Dean: Aerolyn: 182T: Aerolyn Aircraft Company, Single Engine, 1100</div>
    <svg class="lg-chev" style="top:447px" width="10" height="6" viewBox="0 0 10 6"><path d="M1 1l4 4 4-4" stroke="#5cba5c" fill="none"/></svg>
    <div class="lg-rule" style="top:487px;background:#bfeebf"></div>
    <div class="lg-add" style="top:507px"><i class="ring"></i>Add Qualified Pilot -e</div>
    <nav class="tabs" style="top:519px;height:54px">
      <div class="tab active"><svg width="10" height="10" viewBox="0 0 10 10"><circle cx="5" cy="3" r="2.3" fill="currentColor"/><path d="M1 10a4 3.5 0 0 1 8 0z" fill="currentColor"/></svg>Contact</div>
      <div class="tab"><svg width="10" height="10" viewBox="0 0 10 10"><circle cx="5" cy="3" r="2.3" fill="currentColor"/><path d="M1 10a4 3.5 0 0 1 8 0z" fill="currentColor"/></svg>Pilot</div>
      <div class="tab"><svg width="10" height="10" viewBox="0 0 10 10"><path d="M5 0l1 4 4 2v1l-4-1-0.5 2.5 1.5 1V10L5 9.3 3 10v-.5l1.5-1L4 6 0 7V6l4-2z" fill="currentColor"/></svg>Plane</div>
      <div class="tab"><svg width="10" height="10" viewBox="0 0 10 10"><rect x="2" y="3" width="6" height="6" rx="1.5" fill="currentColor"/><rect x="4" y="0" width="2" height="4" fill="currentColor"/></svg>Flt Request</div>
      <div class="tab"><svg width="10" height="10" viewBox="0 0 10 10"><circle cx="2" cy="5" r="1" fill="currentColor"/><circle cx="5" cy="5" r="1" fill="currentColor"/><circle cx="8" cy="5" r="1" fill="currentColor"/></svg>More</div>
    </nav>
    <div class="home" style="left:85px;width:94px;top:565px"></div>
  </section>

  <!-- Contact, redesigned -->
  <section class="phone" style="left:372px;top:618px;width:264px;height:775px">
    <span class="clock">9:41</span>
    <svg class="sys" width="46" height="11" viewBox="0 0 46 11"><rect x="0" y="7" width="2.5" height="4" fill="#000"/><rect x="4" y="5" width="2.5" height="6" fill="#000"/><rect x="8" y="3" width="2.5" height="8" fill="#000"/><rect x="12" y="1" width="2.5" height="10" fill="#000"/><path d="M19 5a6 6 0 0 1 8 0M21 7.5a3 3 0 0 1 4 0" stroke="#000" fill="none" stroke-width="1.5"/><rect x="31" y="2" width="14" height="8" rx="2" fill="#000"/></svg>
    <svg class="top-icon" style="left:11px;top:59px" width="14" height="12" viewBox="0 0 14 12"><path d="M13 6H1M6 1 1 6l5 5" stroke="var(--blue)" fill="none" stroke-width="1.4"/></svg>
    <span class="more" style="top:59px">···</span>
    <div class="avatar" style="left:11px;top:82px;background:var(--green)">DM</div>
    <div class="kicker" style="left:61px;top:89px">Contact</div>
    <div class="headline" style="left:61px;top:109px">Marlow, Dean</div>

    <div class="sec" style="top:153px">Email<span class="act">Add<i class="plus"></i><i class="sep"></i><svg width="8" height="12" viewBox="0 0 8 12"><path d="M1 4l3-3 3 3M1 8l3 3 3-3" stroke="#dde0e6" fill="none"/></svg></span></div>
    <div class="rule" style="top:174px"></div>
    <div class="sec" style="top:195px">Social Media<span class="act">Add<i class="plus"></i><i class="sep"></i><svg width="8" height="12" viewBox="0 0 8 12"><path d="M1 4l3-3 3 3M1 8l3 3 3-3" stroke="#dde0e6" fill="none"/></svg></span></div>
    <div class="rule" style="top:216px"></div>
    <div class="sec" style="top:238px">Emergency Contact<span class="act">Add<i class="plus"></i><i class="sep"></i><svg width="8" height="12" viewBox="0 0 8 12"><path d="M1 4l3-3 3 3M1 8l3 3 3-3" stroke="#dde0e6" fill="none"/></svg></span></div>
    <div class="rule" style="top:259px"></div>
    <div class="sec" style="top:280px">Personal Information<span class="act">Add<i class="plus"></i><i class="sep"></i><svg width="8" height="12" viewBox="0 0 8 12"><path d="M1 4l3-3 3 3M1 8l3 3 3-3" stroke="#dde0e6" fill="none"/></svg></span></div>
    <div class="rule" style="top:301px"></div>
    <div class="sec" style="top:323px">Work Info<span class="act">Add<i class="plus"></i><i class="sep"></i><svg width="8" height="12" viewBox="0 0 8 12"><path d="M1 4l3-3 3 3M1 8l3 3 3-3" stroke="#dde0e6" fill="none"/></svg></span></div>
    <div class="rule" style="top:344px"></div>
    <div class="sec" style="top:366px">Skills/Talents<span class="act">Add<i class="plus"></i><i class="sep"></i><svg width="8" height="12" viewBox="0 0 8 12"><path d="M1 4l3-3 3 3M1 8l3 3 3-3" stroke="#dde0e6" fill="none"/></svg></span></div>
    <div class="rule" style="top:387px"></div>
    <div class="sec" style="top:408px">Resources<span class="act">Add<i class="plus"></i><i class="sep"></i><svg width="8" height="12" viewBox="0 0 8 12"><path d="M1 4l3-3 3 3M1 8l3 3 3-3" stroke="#dde0e6" fill="none"/></svg></span></div>
    <div class="rule" style="top:429px"></div>
    <div class="sec" style="top:451px">Pilots<span class="act"><svg width="8" height="12" viewBox="0 0 8 12"><path d="M1 1l3 3 3-3M1 11l3-3 3 3" stroke="var(--blue)" fill="none"/></svg></span></div>
    <div class="chip" style="top:472px;height:36px">
      <span>Marlow, Dean <span class="dot">•</span> 3647946 <span class="dot">•</span> 0/31/23</span></div>
    <div class="rule" style="top:522px"></div>
    <div class="sec" style="top:543px">Aircraft Owner<span class="act">Add<i class="plus"></i><i class="sep"></i><svg width="8" height="12" viewBox="0 0 8 12"><path d="M1 1l3 3 3-3M1 11l3-3 3 3" stroke="var(--blue)" fill="none"/></svg></span></div>
    <div class="chip" style="top:565px;height:65px">
      <span>Personal <span class="dot">•</span> Marlow, Dean <span class="dot">•</span></span>
      <span>Aerolyn-182T <span class="dot">•</span> Aerolyn Aircraft Company</span>
      <span><span class="dot">•</span> Single Engine, 1100</span></div>
    <div class="rule" style="top:645px"></div>
    <div class="sec" style="top:666px">Qualified Pilot<span class="act">Add<i class="plus"></i><i class="sep"></i><svg width="8" height="12" viewBox="0 0 8 12"><path d="M1 1l3 3 3-3M1 11l3-3 3 3" stroke="var(--blue)" fill="none"/></svg></span></div>
    <div class="chip" style="top:687px;height:51px">
      <span>Marlow, Dean <span class="dot">•</span> Aerolyn-182T <span class="dot">•</span> Aerolyn</span>
      <span>Aircraft Company <span class="dot">•</span> Single Engine, 1100</span></div>
    <div class="indicator" style="left:86px;width:91px;top:765px"></div>
  </section>

  <!-- Pilot, legacy -->
  <section class="legacy" style="left:717px;top:619px;height:569px">
    <div class="status"><span class="time">3:17</span>
      <svg width="30" height="9" viewBox="0 0 30 9"><path d="M4 7a5 5 0 0 1 6 0M2 5a8 8 0 0 1 10 0" stroke="#fff" fill="none" stroke-width="1.3"/><rect x="16" y="1" width="12" height="7" rx="1.5" fill="#fff"/></svg></div>
    <div class="appbar"><svg class="back" width="11" height="11" viewBox="0 0 11 11"><path d="M10 5.5H1M5 1 1 5.5 5 10" stroke="#222" fill="none" stroke-width="1.3"/></svg>Pilot<span class="dots">•••</span></div>
    <div class="card" style="top:78px;height:176px"></div>
    <div class="lg-label" style="left:10px;top:90px">Pilot -e</div>
    <div class="lg-val" style="left:10px;top:101px">Hale, Victor, Owen</div>
    <div class="lg-dots" style="top:101px">•••</div>
    <div class="lg-label" style="left:10px;top:121px">Pilot Certificate No -e</div>
    <div class="lg-val" style="left:10px;top:132px">3182133</div>
    <div class="lg-label" style="left:85px;top:152px">Medical Expiration Date -e</div>
    <div class="lg-val" style="left:85px;top:163px">9/30/24</div>
    <div class="lg-label" style="left:10px;top:183px">Flight Review Expiration Date -e</div>
    <div class="lg-val" style="left:10px;top:193px">6/30/24</div>
    <div class="lg-label" style="left:10px;top:213px">Total Flight Time -e</div>
    <div class="lg-val" style="left:10px;top:224px">2500</div>
    <div class="lg-rule" style="top:249px"></div>
    <div class="card" style="top:263px;height:138px"></div>
    <div class="lg-text" style="top:291px">X35, Pine Shoal Airport, Pine Shoal, FL, 30000, 11, 2500</div>
    <svg class="lg-chev" style="top:279px" width="10" height="6" viewBox="0 0 10 6"><path d="M1 1l4 4 4-4" stroke="#bbb" fill="none"/></svg>
    <div class="lg-rule" style="top:316px"></div>
    <div class="lg-text" style="top:342px">C35, Redmesa Municipal Airport, Redmesa, CO, 80000, 5,334 ft, 4,800 ft</div>
    <svg class="lg-chev" style="top:330px" width="10" height="6" viewBox="0 0 10 6"><path d="M1 1l4 4 4-4" stroke="#bbb" fill="none"/></svg>
    <div class="lg-rule" style="top:369px"></div>
    <div class="lg-add" style="top:389px"><i class="ring"></i>Add Base Airport -e</div>
    <div class="card" style="top:409px;height:30px"></div>
    <div class="lg-add" style="top:427px"><i class="ring"></i>Add Ratings -e</div>
    <div class="card" style="top:445px;height:90px"></div>
    <div class="lg-label" style="left:10px;top:457px">Contact -e</div>
    <div class="lg-val" style="left:10px;top:468px">Nora Hale</div>
    <div class="lg-dots" style="top:468px">•••</div>
    <div class="lg-label" style="left:10px;top:488px">Phone -e</div>
    <div class="lg-val" style="left:10px;top:499px">555-014-2290</div>
    <div class="lg-label" style="left:10px;top:518px">Relationship -e</div>
    <nav class="tabs" style="top:519px;height:50px">
      <div class="tab"><svg width="10" height="10" viewBox="0 0 10 10"><circle cx="5" cy="3" r="2.3" fill="currentColor"/><path d="M1 10a4 3.5 0 0 1 8 0z" fill="currentColor"/></svg>Contact</div>
      <div class="tab active"><svg width="10" height="10" viewBox="0 0 10 10"><circle cx="5" cy="3" r="2.3" fill="currentColor"/><path d="M1 10a4 3.5 0 0 1 8 0z" fill="currentColor"/></svg>Pilot</div>
      <div class="tab"><svg width="10" height="10" viewBox="0 0 10 10"><path d="M5 0l1 4 4 2v1l-4-1-0.5 2.5 1.5 1V10L5 9.3 3 10v-.5l1.5-1L4 6 0 7V6l4-2z" fill="currentColor"/></svg>Plane</div>
      <div class="tab"><svg width="10" height="10" viewBox="0 0 10 10"><rect x="2" y="3" width="6" height="6" rx="1.5" fill="currentColor"/><rect x="4" y="0" width="2" height="4" fill="currentColor"/></svg>Flt Request</div>
      <div class="tab"><svg width="10" height="10" viewBox="0 0 10 10"><circle cx="2" cy="5" r="1" fill="currentColor"/><circle cx="5" cy="5" r="1" fill="currentColor"/><circle cx="8" cy="5" r="1" fill="currentColor"/></svg>More</div>
    </nav>
    <div class="home" style="left:85px;width:94px;top:563px"></div>
  </section>

  <!-- Pilot, redesigned -->
  <section class="phone" style="left:1007px;top:618px;width:265px;height:782px">
    <span class="clock">9:41</span>
    <svg class="sys" width="46" height="11" viewBox="0 0 46 11"><rect x="0" y="7" width="2.5" height="4" fill="#000"/><rect x="4" y="5" width="2.5" height="6" fill="#000"/><rect x="8" y="3" width="2.5" height="8" fill="#000"/><rect x="12" y="1" width="2.5" height="10" fill="#000"/><path d="M19 5a6 6 0 0 1 8 0M21 7.5a3 3 0 0 1 4 0" stroke="#000" fill="none" stroke-width="1.5"/><rect x="31" y="2" width="14" height="8" rx="2" fill="#000"/></svg>
    <svg class="top-icon" style="left:11px;top:59px" width="14" height="12" viewBox="0 0 14 12"><path d="M13 6H1M6 1 1 6l5 5" stroke="var(--blue)" fill="none" stroke-width="1.4"/></svg>
    <span class="more" style="top:59px">···</span>
    <div class="avatar" style="left:12px;top:82px;background:var(--cyan);font-size:12px">HVO</div>
    <div class="kicker" style="left:62px;top:89px">Pilot</div>
    <div class="headline" style="left:62px;top:109px">Hale, Victor, Owen</div>
    <div class="sec" style="top:153px">Pilot Information<span class="act" style="font-weight:800;letter-spacing:1.5px;font-size:13px">···</span></div>
    <div class="f-label" style="top:179px">Pilot Name</div><div class="f-value" style="top:195px">Hale, Victor, Owen</div>
    <div class="f-label" style="top:221px">Pilot Certification Number</div><div class="f-value" style="top:236px">3182133</div>
    <div class="f-label" style="top:263px">Medical Expiration Date</div><div class="f-value" style="top:278px">9/30/24</div>
    <div class="f-label" style="top:305px">Flight Review Expiration Date</div><div class="f-value" style="top:320px">6/30/24</div>
    <div class="f-label" style="top:347px">Total Flight Time</div><div class="f-value" style="top:362px">2500</div>
    <div class="rule" style="top:383px"></div>
    <div class="sec" style="top:405px">Base Airport<span class="act">Add<i class="plus"></i><i class="sep"></i><svg width="8" height="12" viewBox="0 0 8 12"><path d="M1 1l3 3 3-3M1 11l3-3 3 3" stroke="var(--blue)" fill="none"/></svg></span></div>
    <div class="chip" style="top:427px;height:49px">
      <span>X35 <span class="dot">•</span> Pine Shoal Airport <span class="dot">•</span> Pine Shoal, FL,</span>
      <span>30000 <span class="dot">•</span> 11, 2500</span></div>
    <div class="chip" style="top:484px;height:49px">
      <span>C35 <span class="dot">•</span> Redmesa Municipal Airport <span class="dot">•</span></span>
      <span>Redmesa, CO, 80000 <span class="dot">•</span> 5,334 ft, 4,800 ft</span></div>
    <div class="rule" style="top:548px"></div>
    <div class="sec" style="top:569px">Ratings<span class="act">Add<i class="plus"></i><i class="sep"></i><svg width="8" height="12" viewBox="0 0 8 12"><path d="M1 4l3-3 3 3M1 8l3 3 3-3" stroke="#dde0e6" fill="none"/></svg></span></div>
    <div class="rule" style="top:590px"></div>
    <div class="sec" style="top:612px">Contact Information<span class="act" style="font-weight:800;letter-spacing:1.5px;font-size:13px">···</span></div>
    <div class="f-label" style="top:638px">Contact Name</div><div class="f-value" style="top:654px">Nora Hale</div>
    <div class="f-label" style="top:680px">Phone</div><div class="f-value" style="top:695px">555-014-2290</div>
    <div class="f-label" style="top:722px">Relationship</div><div class="f-value" style="top:738px">Brother</div>
    <div class="indicator" style="left:87px;width:91px;top:772px"></div>
  </section>

  <!-- Work order, legacy -->
  <section class="legacy" style="left:1352px;top:619px;height:569px">
    <div class="status"><span class="time">2:16</span>
      <svg width="30" height="9" viewBox="0 0 30 9"><path d="M4 7a5 5 0 0 1 6 0M2 5a8 8 0 0 1 10 0" stroke="#fff" fill="none" stroke-width="1.3"/><rect x="16" y="1" width="12" height="7" rx="1.5" fill="#fff"/></svg></div>
    <div class="appbar"><svg class="back" width="11" height="11" viewBox="0 0 11 11"><path d="M10 5.5H1M5 1 1 5.5 5 10" stroke="#222" fill="none" stroke-width="1.3"/></svg>WorkOrder<span class="dots">•••</span></div>
    <div class="card" style="top:78px;height:36px"></div>
    <div class="tool" style="left:13px"><i></i>Print</div>
    <div class="tool" style="left:59px"><i></i>Create...</div>
    <div class="tool" style="left:104px"><i></i>Create...</div>
    <div class="card" style="top:119px;height:244px"></div>
    <div class="lg-label" style="left:10px;top:131px">Customer -e</div>
    <div class="lg-val" style="left:10px;top:142px">Ferris , Lena</div>
    <div class="lg-dots" style="top:142px">•••</div>
    <div class="lg-label" style="left:10px;top:162px">Service Location -e</div>
    <div class="lg-val" style="left:10px;top:173px">Billing, 48 Willow Ridge Lane , Tarrow :</div>
    <div class="lg-val" style="left:10px;top:184px">TX, 70000</div>
    <div class="lg-label" style="left:10px;top:193px">Billing Address -e</div>
    <div class="lg-val" style="left:10px;top:204px">Billing, 48 Willow Ridge Lane , Tarrow :</div>
    <div class="lg-val" style="left:10px;top:215px">TX, 70000</div>
    <div class="lg-label" style="left:10px;top:224px">Description -e</div>
    <div class="lg-val" style="left:10px;top:234px">Pool maintenance</div>
    <div class="lg-label" style="left:10px;top:254px">Work Order Type -e</div>
    <div class="lg-val" style="left:10px;top:265px">One off job -e</div>
    <div class="lg-label" style="left:10px;top:285px">WO Status -e</div>
    <div class="lg-val" style="left:10px;top:296px">Active -e</div>
    <div class="lg-label" style="left:10px;top:315px">Billing Frequency -e</div>
    <div class="lg-val" style="left:10px;top:326px">Upon job completion -e</div>
    <div class="lg-rule" style="top:351px"></div>
    <div class="card" style="top:371px;height:30px"></div>
    <div class="lg-add" style="top:388px"><i class="ring"></i>Add Technician -e</div>
    <div class="card" style="top:409px;height:30px"></div>
    <div class="lg-add" style="top:426px"><i class="ring"></i>Add Line Items -e</div>
    <div class="abs" style="left:0;right:0;top:441px;height:78px;background:#D5D5D8"></div>
    <nav class="tabs" style="top:519px;height:50px">
      <div class="tab"><svg width="10" height="10" viewBox="0 0 10 10"><circle cx="5" cy="3" r="2.3" fill="currentColor"/><path d="M1 10a4 3.5 0 0 1 8 0z" fill="currentColor"/></svg>Contact</div>
      <div class="tab"><svg width="10" height="10" viewBox="0 0 10 10"><circle cx="5" cy="4" r="3.5" fill="currentColor"/><rect x="2" y="8" width="6" height="2" fill="currentColor"/></svg>Quote</div>
      <div class="tab active"><svg width="10" height="10" viewBox="0 0 10 10"><rect x="0.5" y="3" width="9" height="6.5" rx="1" fill="currentColor"/><rect x="3.5" y="1" width="3" height="2.5" fill="none" stroke="currentColor"/></svg>WorkOrder</div>
      <div class="tab"><svg width="10" height="10" viewBox="0 0 10 10"><circle cx="5" cy="4" r="3.5" fill="currentColor"/><rect x="2" y="8" width="6" height="2" fill="currentColor"/></svg>Invoice</div>
      <div class="tab"><svg width="10" height="10" viewBox="0 0 10 10"><circle cx="2" cy="5" r="1" fill="currentColor"/><circle cx="5" cy="5" r="1" fill="currentColor"/><circle cx="8" cy="5" r="1" fill="currentColor"/></svg>More</div>
    </nav>
    <div class="home" style="left:85px;width:94px;top:563px"></div>
  </section>

  <!-- Work order, redesigned -->
  <section class="phone" style="left:1642px;top:618px;width:265px;height:605px">
    <span class="clock">9:41</span>
    <svg class="sys" width="46" height="11" viewBox="0 0 46 11"><rect x="0" y="7" width="2.5" height="4" fill="#000"/><rect x="4" y="5" width="2.5" height="6" fill="#000"/><rect x="8" y="3" width="2.5" height="8" fill="#000"/><rect x="12" y="1" width="2.5" height="10" fill="#000"/><path d="M19 5a6 6 0 0 1 8 0M21 7.5a3 3 0 0 1 4 0" stroke="#000" fill="none" stroke-width="1.5"/><rect x="31" y="2" width="14" height="8" rx="2" fill="#000"/></svg>
    <svg class="top-icon" style="left:12px;top:59px" width="14" height="12" viewBox="0 0 14 12"><path d="M13 6H1M6 1 1 6l5 5" stroke="var(--blue)" fill="none" stroke-width="1.4"/></svg>
    <svg class="top-icon" style="left:204px;top:59px" width="14" height="14" viewBox="0 0 14 14"><path d="M3.5 5V1h7v4M3.5 10.5H1.5V5h11v5.5h-2M3.5 8.5h7V13h-7z" stroke="var(--blue)" fill="none" stroke-width="1.2"/></svg>
    <span class="more" style="top:59px">···</span>
    <div class="kicker" style="left:12px;top:89px;font-size:12px">Work Order</div>
    <div class="headline" style="left:12px;top:109px">12345ABC</div>
    <div class="sec" style="top:152px">Work Order Information<span class="act" style="font-weight:800;letter-spacing:1.5px;font-size:13px">···</span></div>
    <div class="f-label" style="top:179px">Customer Name</div><div class="f-value" style="top:194px">Ferris, Lena</div>
    <div class="f-label" style="top:221px">Service Location</div><div class="f-value" style="top:243px">Billing, 48 Willow Ridge Lane, Tarrow, TX, 70000</div>
    <div class="f-label" style="top:278px">Billing Address</div><div class="f-value" style="top:300px">Billing, 48 Willow Ridge Lane, Tarrow, TX, 70000</div>
    <div class="f-label" style="top:334px">Description</div><div class="f-value" style="top:350px">Pool maintenance</div>
    <div class="f-label" style="top:376px">Work Order Type</div><div class="f-value" style="top:392px">One off job</div>
    <div class="f-label" style="top:418px">Work Order Status</div><div class="f-value ok" style="top:433px">Active</div>
    <div class="f-label" style="top:460px">Billing Frequency</div><div class="f-value" style="top:475px">Upon job completion</div>
    <div class="rule" style="top:496px"></div>
    <div class="sec" style="top:518px">Technicians<span class="act">Add<i class="plus"></i><i class="sep"></i><svg width="8" height="12" viewBox="0 0 8 12"><path d="M1 4l3-3 3 3M1 8l3 3 3-3" stroke="#dde0e6" fill="none"/></svg></span></div>
    <div class="rule" style="top:539px"></div>
    <div class="sec" style="top:560px">Line Items<span class="act">Add<i class="plus"></i><i class="sep"></i><svg width="8" height="12" viewBox="0 0 8 12"><path d="M1 4l3-3 3 3M1 8l3 3 3-3" stroke="#dde0e6" fill="none"/></svg></span></div>
    <div class="indicator" style="left:88px;width:88px;top:595px"></div>
  </section>

</div>
</body>
</html>
```